Leadership Training Business Needs a business card design

We need a business card designed for our company based in Auckland, New Zealand called Crestfield Guidance Services. We conduct a variety of residential programmes that provide for differnet management levels. These programmes are designed to familiarise managers with important leadership concepts and techniques. This learning is reinforced through the provision of real workplace feedback and the use of action learning opportunities (experiential exercises) to develop the participants' leadership skills and potential. We would like to add our tag line which is:
Inspires Direction - Instils Values - Delivers Results
We would like the card to be a white background but would consider a different background colour on the back. Possibly include the following words on the back:
- Organisational Development
- Positive Cultural Change
- Leadership Programmes
- Practical Development "Tools"
- Crew Balance Inventory
- 360o degree Assessments
- Strengths Based Training
- Coaching and Mentoring

Industry/Entity Type

Business

Requirements
Must have
• Company Name, logo, contact details, website address and email.
• Persons name and their title

```html
<!DOCTYPE html>
<html lang="en">
<head>
<meta charset="utf-8">
<title>Crestfield Guidance Services – Business Card</title>
<link href="https://fonts.googleapis.com/css2?family=Open+Sans:wght@400;600;700&display=swap" rel="stylesheet">
<style>
  :root {
    --stage: #ecebe8;
    --card-white: #f4f5f7;
    --brand-blue: #2f3f98;
    --brand-blue-soft: rgba(255,255,255,0.07);
    --ink: #1d1d22;
    --ink-muted: #555a66;
    --rule: #c9ccd3;
    --white: #ffffff;
    --shadow: 0 14px 30px rgba(0,0,0,0.18);
  }
  * { box-sizing: border-box; margin: 0; padding: 0; }
  html, body { width: 1200px; height: 880px; overflow: hidden; }
  body {
    background: var(--stage);
    font-family: "Open Sans", Arial, sans-serif;
    color: var(--ink);
    position: relative;
  }
  .card {
    position: absolute;
    left: 330px;
    width: 540px;
    height: 310px;
    border-radius: 4px;
    box-shadow: var(--shadow);
    overflow: hidden;
  }

  /* Front */
  .card-front { top: 80px; background: var(--card-white); }
  .brand {
    position: absolute;
    left: 30px; top: 70px;
    width: 230px;
    text-align: center;
  }
  .brand-mark {
    width: 86px; height: 86px;
    border-radius: 50%;
    background: linear-gradient(135deg, #7cb342, #e0a21a);
    margin: 0 auto 12px;
  }
  .brand-name { font-size: 16px; font-weight: 400; color: var(--ink); line-height: 1.2; }
  .brand-sub { font-size: 16px; color: var(--brand-blue); letter-spacing: 0.3px; margin-top: 2px; }

  .contact {
    position: absolute;
    right: 30px; top: 58px;
    width: 230px;
    text-align: right;
  }
  .person-name { font-size: 23px; font-weight: 700; color: var(--brand-blue); line-height: 1.1; }
  .person-title { font-size: 12px; color: var(--ink-muted); margin-top: 2px; }
  .rule { height: 1px; background: var(--rule); margin: 10px 0; }
  .contact-line {
    display: flex; justify-content: flex-end; align-items: center;
    gap: 8px; font-size: 13px; line-height: 22px;
  }
  .contact-line svg { width: 11px; height: 11px; fill: var(--brand-blue); flex: none; }
  .address { display: flex; justify-content: flex-end; align-items: center; gap: 8px; }
  .address-text { font-size: 13px; line-height: 20px; }
  .address svg { width: 12px; height: 16px; fill: var(--brand-blue); }

  /* Back */
  .card-back { top: 490px; background: var(--brand-blue); color: var(--white); }
  .back-glow {
    position: absolute; left: 60px; top: -90px;
    width: 300px; height: 300px; border-radius: 50%;
    background: var(--brand-blue-soft);
  }
  .back-brand {
    position: absolute; left: 30px; top: 34px; width: 230px; text-align: center;
  }
  .back-mark {
    width: 70px; height: 70px; border-radius: 50%;
    background: var(--white); margin: 0 auto 12px;
  }
  .back-name { font-size: 16px; line-height: 1.25; }
  .services {
    position: absolute; left: 290px; top: 28px;
    list-style: none; font-size: 14px; line-height: 24px;
  }
  .services li::before { content: "• "; }
  .back-rule {
    position: absolute; left: 30px; right: 30px; top: 238px;
    height: 1px; background: rgba(255,255,255,0.7);
  }
  .tagline {
    position: absolute; left: 0; right: 0; top: 252px;
    text-align: center; font-size: 15px; font-weight: 700; letter-spacing: 0.3px;
  }
</style>
</head>
<body>

<section class="card card-front" aria-label="Business card front">
  <div class="brand">
    <div class="brand-mark"></div>
    <div class="brand-name">Crestfield Guidance Services</div>
    <div class="brand-sub">Leadership Programmes</div>
  </div>

  <div class="contact">
    <div class="person-name">Name Surname</div>
    <div class="person-title">manager</div>
    <div class="rule"></div>
    <div class="contact-line">+00 123 45 789
      <svg viewBox="0 0 10 10"><rect x="2.5" y="0" width="5" height="10" rx="1"/></svg></div>
    <div class="contact-line">+00 123 45 789
      <svg viewBox="0 0 10 10"><rect x="2" y="0" width="6" height="3"/><rect x="0" y="3.5" width="10" height="4.5" rx="1"/><rect x="2" y="8" width="6" height="2"/></svg></div>
    <div class="contact-line">office@yourdomain.com
      <svg viewBox="0 0 10 10"><rect x="0" y="2" width="10" height="6.5" rx="1"/></svg></div>
    <div class="contact-line">www.yourdomain.com
      <svg viewBox="0 0 10 10"><circle cx="5" cy="5" r="4.4" fill="none" stroke="#2f3f98" stroke-width="1"/><ellipse cx="5" cy="5" rx="2" ry="4.4" fill="none" stroke="#2f3f98" stroke-width="0.8"/><line x1="0.6" y1="5" x2="9.4" y2="5" stroke="#2f3f98" stroke-width="0.8"/></svg></div>
    <div class="rule"></div>
    <div class="address">
      <div class="address-text">Your Address Goes Here<br>City, Country Zipcode</div>
      <svg viewBox="0 0 12 16"><path d="M6 0a6 6 0 0 0-6 6c0 4.5 6 10 6 10s6-5.5 6-10a6 6 0 0 0-6-6zm0 8.5A2.5 2.5 0 1 1 6 3.5a2.5 2.5 0 0 1 0 5z"/></svg>
    </div>
  </div>
</section>

<section class="card card-back" aria-label="Business card back">
  <div class="back-glow"></div>
  <div class="back-brand">
    <div class="back-mark"></div>
    <div class="back-name">Crestfield Guidance Services<br>Leadership Programmes</div>
  </div>
  <ul class="services">
    <li>Organisational Development</li>
    <li>Positive Cultural Change</li>
    <li>Leadership Programmes</li>
    <li>Practical Development "Tools"</li>
    <li>Crew Balance Inventory</li>
    <li>360 Degree Assessments</li>
    <li>Strengths Based Training</li>
    <li>Coaching and Mentoring</li>
  </ul>
  <div class="back-rule"></div>
  <div class="tagline">Inspires Direction • Instils Values • Delivers Results</div>
</section>

</body>
</html>
```